TeeVault - In Need of Logo/Packaging Design

I am looking for a logo and packaging design for my new company, "TeeVault". TeeVault is monthly subscription box that delivers golf equipment and accessories directly to the customer's door. The box will be a standard craft material Roll End Front Tuck mailer - the dimensions of the box are as follows:

9"x12"x3.5" (LxWxH)

I would like to see a simple and modern design that ultimately communicates innovation and creativity with the sport of golf. The box will be standard craft cardboard material therefore I would like to incorporate colors with good contrast; I am visualizing black/gray/white but am open to other options as well. If possible I would also like to incorporate the following slogan in some way:

Gear For Every Round

I've attached a couple logos that I found online which I really like so you can get an idea of what I am looking for.

Thank you!

Target Market(s)

The upcoming young, millennial golfer.

Industry/Entity Type

Sporting Good

Logo Text

TeeVault

Requirements
Must have
• Logo/packaging design

```html
<!DOCTYPE html>
<html lang="en">
<head>
<meta charset="utf-8">
<title>TeeVault Mailer Box Dieline</title>
<link rel="stylesheet" href="https://fonts.googleapis.com/css2?family=Open+Sans:wght@400&family=Cormorant+Garamond:wght@500&display=swap">
<style>
  :root {
    --canvas: #ffffff;
    --panel-orange: #ff7f00;
    --panel-purple: #7f68a9;
    --label: #ffffff;
    --badge: #000000;
    --cut-line: #ff3b3b;
    --fold-line: #9b4fc0;
  }
  html, body {
    margin: 0;
    padding: 0;
    width: 1143px;
    height: 1200px;
    overflow: hidden;
    background: var(--canvas);
  }
  .dieline-canvas { display: block; width: 1143px; height: 1200px; }
  .panel { fill: var(--panel-fill); }
  .brand-badge { fill: var(--badge); }
  .panel-label {
    fill: var(--label);
    font-family: "Open Sans", Arial, sans-serif;
    font-weight: 400;
  }
  .brand-name, .brand-tagline {
    fill: var(--label);
    font-family: "Cormorant Garamond", Georgia, serif;
    font-weight: 500;
  }
  .cut-line { fill: none; stroke: var(--cut-line); stroke-width: 1; }
  .fold-line { fill: none; stroke: var(--fold-line); stroke-width: 1; }
  .box-full { --panel-fill: var(--panel-orange); }
  .box-thumbnail { --panel-fill: var(--panel-purple); }
</style>
</head>
<body>
<svg class="dieline-canvas" viewBox="0 0 1143 1200" xmlns="http://www.w3.org/2000/svg">
  <defs>
    <g id="box-dieline">
      <!-- front inside flap row -->
      <path class="panel" d="M144,22 H240 V158 L144,140 Z"/>
      <rect class="panel" x="251" y="22" width="465" height="136"/>
      <path class="panel" d="M726,22 H823 V140 L726,158 Z"/>
      <rect class="brand-badge" x="288" y="30" width="393" height="118"/>
      <text class="panel-label" x="260" y="50" font-size="16">FRONT INSIDE FLAP</text>
      <text class="brand-name" x="484" y="116" font-size="66" text-anchor="middle">TeeVault</text>

      <!-- main row -->
      <rect class="panel" x="30" y="173" width="98" height="348"/>
      <rect class="panel" x="144" y="172" width="96" height="349"/>
      <rect class="panel" x="251" y="172" width="465" height="349"/>
      <rect class="panel" x="726" y="172" width="97" height="349"/>
      <rect class="panel" x="841" y="172" width="97" height="349"/>
      <text class="panel-label" font-size="21" text-anchor="middle" transform="translate(84,345) rotate(90)">
        <tspan x="0" y="-6">LEFT INSIDE</tspan><tspan x="0" y="22">TUCK FLAP</tspan>
      </text>
      <text class="panel-label" font-size="21" text-anchor="middle" transform="translate(190,353) rotate(90)" y="7">LEFT</text>
      <text class="panel-label" x="476" y="348" font-size="22" text-anchor="middle">BOTTOM</text>
      <text class="panel-label" font-size="21" text-anchor="middle" transform="translate(776,340) rotate(-90)" y="7">RIGHT</text>
      <text class="panel-label" font-size="21" text-anchor="middle" transform="translate(882,357) rotate(-90)">
        <tspan x="0" y="-6">RIGHT  INSIDE</tspan><tspan x="0" y="22">TUCK FLAP</tspan>
      </text>

      <!-- back row -->
      <path class="panel" d="M144,548 L240,535 V668 H144 Z"/>
      <rect class="panel" x="251" y="535" width="465" height="133"/>
      <path class="panel" d="M726,535 L823,548 V668 H726 Z"/>
      <rect class="brand-badge" x="288" y="544" width="393" height="117"/>
      <text class="panel-label" x="253" y="564" font-size="16">BACK</text>
      <text class="brand-name" x="484" y="630" font-size="66" text-anchor="middle">TeeVault</text>

      <!-- top row -->
      <path class="panel" d="M240,678 V1026 H234 Q144,1020 144,950 V760 Q144,684 234,678 Z"/>
      <rect class="panel" x="251" y="678" width="465" height="348"/>
      <path class="panel" d="M726,678 H733 Q823,684 823,760 V950 Q823,1020 733,1026 H726 Z"/>
      <rect class="brand-badge" x="288" y="758" width="393" height="186"/>
      <text class="panel-label" x="272" y="724" font-size="20">TOP</text>
      <text class="brand-name" x="484" y="860" font-size="66" text-anchor="middle">TeeVault</text>
      <text class="brand-tagline" x="484" y="910" font-size="20" text-anchor="middle">Gear For Every Round</text>
      <text class="panel-label" font-size="21" text-anchor="middle" transform="translate(190,852) rotate(90)">
        <tspan x="0" y="-6">LEFT TOP INSIDE</tspan><tspan x="0" y="22">TUCK FLAP</tspan>
      </text>
      <text class="panel-label" font-size="21" text-anchor="middle" transform="translate(772,852) rotate(-90)">
        <tspan x="0" y="-6">RIGHT TOP INSIDE</tspan><tspan x="0" y="22">TUCK FLAP</tspan>
      </text>

      <!-- front flap row -->
      <path class="panel" d="M144,1043 L240,1040 V1175 H228 Q150,1130 144,1043 Z"/>
      <rect class="panel" x="251" y="1040" width="465" height="135"/>
      <path class="panel" d="M726,1040 L823,1043 Q817,1130 739,1175 H726 Z"/>
      <text class="panel-label" x="460" y="1107" font-size="22" text-anchor="middle">FRONT FLAP</text>
    </g>
  </defs>

  <path class="cut-line" d="M124,4 H722 L735,10 H840 V160 H962 V555 H845 V1150 Q845,1198 800,1198 H168 Q122,1198 122,1150 V555 H4 V137 H124 Z"/>
  <path class="fold-line" d="M132,12 H720 L730,17 H832 V166 H948 V528 H832 V1150 Q832,1190 795,1190 H172 Q130,1190 130,1150 V528 H19 V164 H132 Z"/>

  <use href="#box-dieline" class="box-full"/>
  <use href="#box-dieline" class="box-thumbnail" transform="translate(848.6,821) scale(0.314)"/>
</svg>
</body>
</html>
```